・電子書籍の表紙デザインをお願いします。

・本の内容
モヤモヤグルグルしてるただの主婦でも、天職につながれば稼げるようになる。
自分の事を理解し天職につながることによって、
自信や人間関係やお金、仕事や健康までも、うまく回り始める。
私のエピソードから天職につながるプロセスを見てもらって解説してます。
後半で、あなたの天職につながるワークを実践して
スモールステップを踏み出せるようになるという内容になっています。

・デザイン要望
文字を大きく、パッと見て何が書いてあるかわかりやすいようにして欲しいです。

その他何かありましたら、気軽に質問して下さいね。
よろしくお願いいたします。

タイトルとして

スル~っととんとん拍子に
『ひらめく毎日!をひらく本』
モヤモヤグルグルしてたただの主婦の私が、
まさかの経営者になった理由
森川遥香

読者限定プレゼント
「何かしたい」でも「何をしたいのかわからない」
そんなあなたに
「星読みカルテ」プレゼント

入れて欲しいです。
とんとん拍子 → トントン拍子

軽快なイメージに一番近かったです。

皆さんのご提案、すべて素敵で迷いました。
ありがとうございました。

```html
<!DOCTYPE html>
<html lang="ja">
<head>
<meta charset="UTF-8">
<title>ひらめく毎日!をひらく本</title>
<link href="https://fonts.googleapis.com/css2?family=M+PLUS+Rounded+1c:wght@500;700;800;900&display=swap" rel="stylesheet">
<style>
:root{
  --yellow:#f6c600;
  --sky:#5ec6ea;
  --ink:#1d1d1d;
  --white:#ffffff;
  --green:#4cc21a;
  --pink:#ee2f7f;
  --orange:#f08a1c;
  --lemon:#fff35a;
  --skin-a:#f2d2b8;
  --skin-b:#e9b896;
}
*{margin:0;padding:0;box-sizing:border-box}
html,body{width:750px;height:1200px;overflow:hidden}
body{font-family:"M PLUS Rounded 1c",sans-serif;color:var(--ink)}
.cover{position:relative;width:750px;height:1200px;overflow:hidden;background:var(--sky)}
.backdrop{position:absolute;inset:0}
.hand-photo{position:absolute;left:400px;top:40px;width:320px;height:600px;
  background:linear-gradient(165deg,var(--skin-a) 0%,var(--skin-b) 60%,var(--yellow) 100%);
  border-radius:140px 140px 60px 60px;opacity:.9}
.line{position:absolute;white-space:nowrap}
.tagline{left:88px;top:4px;font-weight:900;color:var(--white);font-size:68px;letter-spacing:1px}
.tagline-2{left:200px;top:100px;font-weight:800;font-size:50px;line-height:1}
.tagline-2 .soft{color:var(--white);font-size:38px;vertical-align:8px}
.title{left:12px;top:180px;font-weight:900;font-size:108px;line-height:125px;letter-spacing:-2px;white-space:nowrap}
.title .accent{color:var(--green)}
.author{left:12px;top:592px;font-weight:700;font-size:28px}
.story{font-weight:900;font-size:38px;line-height:1}
.story .pink{color:var(--pink)}
.story .orange{color:var(--orange)}
.story-1{left:512px;top:660px}
.story-2{left:548px;top:708px}
.story-3{left:650px;top:754px;font-size:26px}
.story-4{left:630px;top:786px}
.story-5{left:512px;top:834px}
.story-6{left:512px;top:884px}
.story-7{left:512px;top:934px}
.story-8{left:512px;top:986px}
.gift-label{left:95px;top:800px;color:var(--pink);font-weight:900;font-size:32px;
  transform:rotate(-10deg);transform-origin:left center;z-index:2}
.gift-badge{position:absolute;left:-40px;top:860px;width:530px;height:390px;border-radius:50%;background:var(--pink)}
.gift-text{position:absolute;left:55px;top:910px;width:400px;transform:rotate(-10deg);transform-origin:left top;
  color:var(--white);font-weight:800;font-size:30px;line-height:1.3;z-index:2}
.gift-text .quote{color:var(--lemon)}
.gift-text .lead{font-size:24px}
.gift-text .prize{color:var(--lemon);font-size:40px;font-weight:900}
</style>
</head>
<body>
<main class="cover">
  <svg class="backdrop" width="750" height="1200" viewBox="0 0 750 1200" aria-hidden="true">
    <rect width="750" height="1200" fill="var(--sky)"/>
    <polygon points="0,0 750,0 750,430 0,830" fill="var(--yellow)"/>
  </svg>

  <div class="hand-photo" role="img" aria-label="ピースサインをする手と黄色い袖の写真"></div>

  <p class="line tagline">スル〜〜〜っと</p>
  <p class="line tagline-2"><span class="soft">トントン</span>拍子に</p>

  <h1 class="line title">ひらめく<br><span class="accent">毎日!</span>を<br>ひらく本</h1>

  <p class="line author">【著者】森川遥香</p>

  <div class="story">
    <p class="line story-1">モヤモヤ</p>
    <p class="line story-2">グルグル</p>
    <p class="line story-3">してた</p>
    <p class="line story-4">ただの</p>
    <p class="line story-5"><span class="pink">主婦</span>の私が、</p>
    <p class="line story-6">まさかの</p>
    <p class="line story-7"><span class="orange">経営者に</span></p>
    <p class="line story-8">なった理由</p>
  </div>

  <div class="gift-badge" aria-hidden="true"></div>
  <p class="line gift-label">読者限定プレゼント</p>
  <div class="gift-text">
    <span class="quote">「何かしたい!!」</span>でも、<br>
    <span class="quote">「自分が何したいのかが</span><br>
    <span class="quote">わからない!」</span><br>
    <span class="lead">そんなあなた自身を活かす</span><br>
    <span class="prize">星読みカルテ付き</span>
  </div>
</main>
</body>
</html>
```